"Drink Champagne and Dance on the Table" sort of business card needed!

We throw events, weddings, engagement parties, baby showers and the sort of end of year corporate events that people remember long after the glitter has settled - the sort of events that make you stand still and say wow when you walk in and then make you want to "Drink Champagne and Dance on the Tables"

We have a great logo with heaps of potential and need a business card that just screams creative professionals!

We are based in Auckland, NZ and are priced at the Premium end of the market were there are around 10 other main competitors. We need to stand out and make a strong statement about who we are!

Our Business Card will be one of the few items that we print out so are fully prepared to invest in a premium print job.

We really love our logo and think it has heaps of potential! Its ok if you would like to manipulate it (maybe put it on an angle, or use the circle element on its own?).

Black and Gold is very striking, but its very done in our market so we would like to avoid a solid black background please

We have done a bit of an inspiration document to give you an idea of the sort of look and feel we are hoping to achieve.

Target Market(s)

Woman aged 30 - 45 with an income bracket of $70k +

Industry/Entity Type

Event Planning

Contact Information for Business Card

Marnie
hello@fennoriwick.co.nz
www.fennoriwick.co.nz
02734419027

Number of Pages Required

5+ page

Requirements
Must have
• Vibrant colours and design (we love the vibrant pink and gold in the inspiration file)
• We would love to see some colour and creativity (although the black and gold is very striking). Because we are doing such minimal print work I am happy for the cards to be a little more expensive so if you want to use cut outs, rounded corners, gold foil, non standard size etc I am happy for that too. I really want the wow factor.
Nice to have
• We would like the design to be double sided.
Should not have
• The logo colour changed
• Use of Purple or Green or solid black background.
• Wedding Photos!

```html
<!DOCTYPE html>
<html lang="en">
<head>
<meta charset="utf-8">
<title>Fenno and Riwick – Folded Business Card</title>
<link rel="stylesheet" href="https://fonts.googleapis.com/css2?family=Cormorant+Garamond:wght@600&family=Montserrat:wght@500&family=Lobster&family=Libre+Baskerville&display=swap">
<style>
  :root {
    --stage: #1d1b1b;
    --pink: #ec2f78;
    --paper: #ffffff;
    --fold-shade: #f1efef;
    --gold: #c59d3f;
    --gold-light: #e2c572;
  }
  * { margin: 0; padding: 0; box-sizing: border-box; }
  html, body { width: 1200px; height: 800px; overflow: hidden; }
  body {
    background: var(--stage);
    position: relative;
    font-family: "Libre Baskerville", serif;
  }
  .card-panel {
    position: absolute;
    top: 150px;
    width: 300px;
    height: 496px;
    border-radius: 16px;
    display: flex;
    flex-direction: column;
    align-items: center;
  }
  .front-cover { left: 90px; background: var(--pink); }
  .inside-spread {
    position: absolute;
    top: 150px;
    left: 520px;
    width: 590px;
    height: 496px;
    display: flex;
    border-radius: 16px;
    overflow: hidden;
    background: var(--paper);
  }
  .inside-left {
    width: 295px;
    height: 100%;
    background: linear-gradient(90deg, var(--paper) 85%, var(--fold-shade));
  }
  .inside-right {
    width: 295px;
    height: 100%;
    border-left: 1px solid #e4e1e1;
    display: flex;
    flex-direction: column;
    align-items: center;
  }

  .brand-circle { display: block; }
  .front-cover .brand-circle { margin-top: 92px; }
  .inside-right .brand-circle { margin-top: 36px; }

  .brand-name {
    font-family: "Cormorant Garamond", serif;
    font-weight: 600;
    color: var(--gold);
    letter-spacing: 0.5px;
    white-space: nowrap;
  }
  .front-cover .brand-name { font-size: 40px; margin-top: 52px; color: var(--gold-light); }
  .inside-right .brand-name { font-size: 32px; margin-top: 8px; }

  .tagline {
    display: flex;
    align-items: center;
    gap: 8px;
    font-family: "Montserrat", sans-serif;
    font-weight: 500;
    letter-spacing: 3px;
    color: var(--gold);
    white-space: nowrap;
  }
  .tagline::before, .tagline::after {
    content: "";
    display: block;
    width: 18px;
    height: 1px;
    background: currentColor;
  }
  .front-cover .tagline { font-size: 10px; color: var(--gold-light); margin-top: 2px; }
  .inside-right .tagline { font-size: 8px; margin-top: 0; }

  .person-name {
    font-family: "Lobster", sans-serif;
    font-size: 34px;
    color: var(--gold);
    margin-top: 60px;
  }
  .contact-icons { margin-top: 34px; display: block; }
  .contact-list {
    list-style: none;
    text-align: center;
    margin-top: 30px;
    font-size: 11px;
    line-height: 24px;
    color: var(--gold);
  }
</style>
</head>
<body>

  <section class="card-panel front-cover" aria-label="Card front cover">
    <svg class="brand-circle" width="180" height="180" viewBox="0 0 180 180" aria-hidden="true">
      <circle cx="90" cy="90" r="86" fill="none" stroke="var(--gold-light)" stroke-width="4"/>
    </svg>
    <h1 class="brand-name">Fenno and Riwick</h1>
    <p class="tagline">WEDDINGS&amp;EVENTS</p>
  </section>

  <section class="inside-spread" aria-label="Card inside">
    <div class="inside-left"></div>
    <div class="inside-right">
      <svg class="brand-circle" width="88" height="88" viewBox="0 0 88 88" aria-hidden="true">
        <circle cx="44" cy="44" r="41" fill="none" stroke="var(--gold)" stroke-width="3"/>
      </svg>
      <h2 class="brand-name">Fenno and Riwick</h2>
      <p class="tagline">WEDDINGS&amp;EVENTS</p>
      <p class="person-name">Marnie</p>
      <svg class="contact-icons" width="160" height="18" viewBox="0 0 160 18" aria-hidden="true">
        <line x1="0" y1="9" x2="160" y2="9" stroke="var(--gold)" stroke-width="1"/>
        <circle cx="54" cy="9" r="8" fill="var(--gold)"/>
        <path d="M50.5 5.5 q1-1 2 0 l1 1.5 q.3.7-.3 1.2 q.8 1.8 2.6 2.6 q.5-.6 1.2-.3 l1.5 1 q1 1 0 2 q-1.5 1.3-4-.3 q-3.2-2.2-4.3-4.9 q-.8-1.8.3-2.8z" fill="var(--paper)"/>
        <circle cx="80" cy="9" r="8" fill="var(--gold)"/>
        <rect x="75.5" y="5.8" width="9" height="6.4" rx="1" fill="var(--paper)"/>
        <path d="M75.8 6.2 L80 9.4 L84.2 6.2" fill="none" stroke="var(--gold)" stroke-width="0.9"/>
        <circle cx="106" cy="9" r="8" fill="var(--gold)"/>
        <circle cx="106" cy="9" r="4.6" fill="none" stroke="var(--paper)" stroke-width="1"/>
        <ellipse cx="106" cy="9" rx="2" ry="4.6" fill="none" stroke="var(--paper)" stroke-width="0.9"/>
        <line x1="101.4" y1="9" x2="110.6" y2="9" stroke="var(--paper)" stroke-width="0.9"/>
      </svg>
      <ul class="contact-list">
        <li>02734419027</li>
        <li>hello@fennoriwick.co.nz</li>
        <li>www.fennoriwick.co.nz</li>
      </ul>
    </div>
  </section>

</body>
</html>
```